TKA Electricial Contracting Services

Hi guys, after a design for my small electrical company, have logo design files to be incorporated into the layout, the basic concept is electrical contracting services for residential, commercial, industrial & data services, image is clean clear and strong,

Card format is to have a nice clean logo on front,with maybe the Residential – commercial – industrial - data, followed with licensed & insured, followed by contact details on backside of the card.

Target Market(s)

Residential, commercial, industrial sectors.

Industry/Entity Type

Electrical

Contact Information for Business Card

TKA logo,
Residential – commercial – industrial - data
REC: 61372
Email: tka@poralink.net.au
Phone: 0458 203 719

Requirements
Must have
• Clean & strong design.
Nice to have
• If possible, I would like the logo colours inverted so the text is orange and the background is black on the front of the card, then the backside of the card be the reverse colour
Should not have
• No Sparks, lightning bolts,

```html
<!DOCTYPE html>
<html lang="en">
<head>
<meta charset="utf-8">
<title>Tyler Kane Electrical Business Card</title>
<link rel="stylesheet" href="https://fonts.googleapis.com/css2?family=Open+Sans:wght@400;700&family=Roboto:wght@700&display=swap">
<style>
  :root {
    --stage: #6e4232;
    --ink: #0b0b0c;
    --orange: #e5762a;
    --divider: #b3561a;
  }
  html, body {
    margin: 0;
    padding: 0;
    width: 1200px;
    height: 900px;
    overflow: hidden;
    background: var(--stage);
  }
  .canvas {
    position: relative;
    width: 1200px;
    height: 900px;
  }
  .card {
    position: absolute;
    top: 319px;
    width: 443px;
    height: 260px;
    border-radius: 16px;
    overflow: hidden;
  }
  .card--back { left: 129px; background: var(--ink); }
  .card--front { left: 629px; background: var(--orange); }

  .brand-name {
    position: absolute;
    left: 0;
    right: 0;
    margin: 0;
    text-align: center;
    font-family: "Open Sans", sans-serif;
    font-weight: 700;
    line-height: 1.1;
  }
  .card--back .brand-name {
    top: 116px;
    font-size: 17px;
    color: var(--orange);
  }
  .card--front .brand-name {
    top: 106px;
    font-size: 34px;
    color: var(--ink);
  }

  .licence {
    position: absolute;
    left: 0;
    right: 0;
    top: 196px;
    margin: 0;
    text-align: center;
    font-family: "Open Sans", sans-serif;
    font-weight: 400;
    font-size: 10px;
    letter-spacing: 0.6px;
    color: var(--orange);
  }

  .contact-band {
    position: absolute;
    left: 0;
    right: 0;
    bottom: 0;
    height: 28px;
    background: var(--orange);
    display: flex;
    align-items: center;
    font-family: "Open Sans", sans-serif;
    font-size: 13.5px;
    color: var(--ink);
  }
  .contact-band__item { flex: 1; text-align: center; }
  .contact-band__divider {
    width: 1px;
    height: 20px;
    background: var(--divider);
  }

  .services-band {
    position: absolute;
    left: 0;
    right: 0;
    bottom: 0;
    height: 17px;
    background: var(--ink);
    display: flex;
    align-items: center;
    justify-content: center;
    font-family: "Roboto", sans-serif;
    font-weight: 700;
    font-size: 7.5px;
    letter-spacing: 0.4px;
    color: var(--orange);
  }
</style>
</head>
<body>
<main class="canvas">
  <section class="card card--back" aria-label="Card back">
    <p class="brand-name">Tyler Kane Electrical</p>
    <p class="licence">LICENSED &amp; INSURED &nbsp;·&nbsp; REC 61372</p>
    <div class="contact-band">
      <span class="contact-band__item">P : +61 0458 203 719</span>
      <span class="contact-band__divider"></span>
      <span class="contact-band__item">E : tka@poralink.net.au</span>
    </div>
  </section>

  <section class="card card--front" aria-label="Card front">
    <p class="brand-name">Tyler Kane Electrical</p>
    <div class="services-band">RESIDENTIAL &nbsp;–&nbsp; COMMERCIAL &nbsp;–&nbsp; INDUSTRIAL &nbsp;-&nbsp; DATA</div>
  </section>
</main>
</body>
</html>
```